International Health Supplement Company Needs Packaging and Label Redesign

Copperfield Vitals LLC requires a redesign for 1 internationally sold product and accompanying designs for 5 additional products. The additional products are currently sold locally and yet to be released internationally.

Our company is honest, premium, and passionate about supplements. We adopt a 'no BS' stance and as such source only the finest ingredients and deliver high-quality liquid health supplements to customers globally. We do not compromise on quality and do not apologise for price.

We want a clean, crisp design that conveys ‘premium, cutting-edge, boutique’ at a glance. We feel our current design appeals more to the 'chest beaters' rather than the 'chess players' that our research has indicated are our customers.

We have SIX PRODUCTS TOTAL in our range and feel individual color cues to distinguish the different products would greatly assist customer navigation i.e. Customers will identify ‘red’ means ‘product X’ without reading the label. (Examples attached and below we believe do this well).

Current 30ml bottle, cap, and dropper are in black and will remain so. Current label is black, however, we have a white label on our local product (example attached) and prefer the look of it.

Packaging is currently black and could remain so however most products that appeal to our target market are in white with color accents.

One consideration we have is that the product up until now has been selling exceptionally well so we need to retain some kind of familiarity with the existing branding. Perhaps that’s just the logo.

Logo can be revised i.e. add company name and/or company slogan.

Products are: (Function - Name)

Testosterone Support - Tongkat Ali (current)
Hormone Support - Jiaogulan
Energy Support - Ashwaghanda
Libido Support - Krachai Dam (for men)
Libido Support - Kacip Fatimah (for women)
Sleep Support - Wild Chamomile

Packaging: 4.6cm (L) x 8.0cm (W) x 11.2cm (H)
Label: 30 mL bottle

https://www.portfolioshelf.example/gallery/TONIC-BOX-STUDY-2012/8824160
http://www.pelrostudio.example/projects/#/harbor-tea/
https://www.portfolioshelf.example/gallery/57730482/Velmora-Skin
https://au.pinboardly.example/pin/913402775610238841/
https://au.pinboardly.example/pin/61470329814550298/
http://kelvo.studio.example/en/portfolio/logo-redesign/

Target Market(s)

Generation X Men (and their partners), 36-55, upper middle class, who appreciate quality products.

Industry/Entity Type

Health Product

Font styles to use
Serif
Sans Serif

Requirements
Must have
• Packaging - Principal Display Panel (Front):
• 1. Function & Name of each product i.e 'Testosterone Support' & 'Tongkat Ali'
• 2. '30ml' AND '1 fl oz' (text size 1.8in / 3.2mm / 9 point min.)
• 3. 'Dietary Supplement'
• Packaging - Information Panel (Right):
• 1. Supplement Facts Panel (template accepted for drafts)
• 2. Directions: (lorum ipsum accepted for drafts)
• 3. Safety Warning: (lorum ipsum accepted for drafts)
• 4. 'Manufactured for: Copperfield Vitals LLC'
• 5. 'Sheridan, Wyoming'
• 6. '(307) 641 3528'
• 7. 'Product of Thailand'
• Bottle Label:
• 3. 'Dietary Supplement'
• 4. Supplement Facts Panel (template accepted for drafts)
• 5. Directions: (lorum ipsum accepted for drafts)
• 6. Safety Warning: (forum ipsum accepted for drafts)
• 7. 'Manufactured for: Copperfield Vitals LLC'
• 8. 'Sheridan, Wyoming'
• 9. '(307) 641 3528'
• 10. 'Product of Thailand'
Nice to have
• Updated logo with company name 'Copperfield Vitals' and/or company slogan 'Quality Without Compromise' added.
Should not have
• No photos or stock images.
• No elements of the current design (excluding logo) to remain i.e. 'Otter Finn', 'Testosterone Booster', 'Increase Lean Muscle', 'Stabilise Hormones', 'Boost Endurance', 'Improve Muscle Naturally', are all to be omitted.

```html
<!DOCTYPE html>
<html lang="en">
<head>
<meta charset="UTF-8">
<title>Wild Chamomile – Bottle Label</title>
<link rel="stylesheet" href="https://fonts.googleapis.com/css2?family=Montserrat:wght@300;400;500&display=swap">
<style>
  :root {
    --bg: #e6e7e8;
    --label: #ffffff;
    --teal: #1f9a92;
    --teal-soft: #cfe9e7;
    --rule: #5dbdb5;
    --ink: #4a4d50;
  }
  html, body {
    margin: 0;
    width: 1200px;
    height: 900px;
    overflow: hidden;
    background: var(--bg);
    font-family: "Montserrat", Arial, sans-serif;
  }
  .canvas {
    position: relative;
    width: 1200px;
    height: 900px;
  }
  .label {
    position: absolute;
    left: 310px;
    top: 70px;
    width: 580px;
    height: 760px;
    background: var(--label);
    box-shadow: 0 2px 14px rgba(0,0,0,0.08);
  }
  .floral-decoration {
    position: absolute;
    right: 0;
    top: 40px;
    width: 260px;
    height: 340px;
    background: radial-gradient(circle at 45% 40%, var(--teal-soft) 0%, rgba(207,233,231,0.45) 45%, rgba(255,255,255,0) 72%);
  }
  .brand {
    position: absolute;
    right: 48px;
    top: 96px;
    display: flex;
    align-items: center;
    gap: 10px;
    color: var(--teal);
    font-weight: 400;
    font-size: 15px;
    letter-spacing: 0.04em;
  }
  .brand-dot {
    width: 34px;
    height: 34px;
    border-radius: 50%;
    background: var(--teal);
  }
  .product-name {
    position: absolute;
    left: 40px;
    top: 150px;
    margin: 0;
    color: var(--teal);
    font-weight: 400;
    font-size: 64px;
    line-height: 60px;
    letter-spacing: 0.01em;
  }
  .product-function {
    position: absolute;
    left: 42px;
    top: 290px;
    margin: 0;
    color: var(--ink);
    font-weight: 400;
    font-size: 27px;
    letter-spacing: 0.08em;
  }
  .rule {
    position: absolute;
    left: 0;
    width: 100%;
    height: 2px;
    background: var(--rule);
  }
  .rule.r1 { top: 345px; }
  .rule.r2 { top: 494px; }
  .rule.r3 { top: 556px; }
  .rule.r4 { top: 718px; }
  .description {
    position: absolute;
    left: 54px;
    top: 362px;
    margin: 0;
    color: var(--ink);
    font-weight: 300;
    font-size: 21px;
    line-height: 38px;
  }
  .benefit {
    position: absolute;
    left: 54px;
    top: 510px;
    margin: 0;
    color: var(--teal);
    font-weight: 400;
    font-size: 21px;
    letter-spacing: 0.02em;
  }
  .facts-table {
    position: absolute;
    left: 0;
    top: 556px;
    width: 100%;
    height: 162px;
  }
  .facts-table .cell-divider {
    position: absolute;
    left: 380px;
    top: 0;
    width: 2px;
    height: 100%;
    background: var(--rule);
  }
  .facts-table .row-divider {
    position: absolute;
    left: 0;
    top: 58px;
    width: 380px;
    height: 2px;
    background: var(--rule);
  }
  .supplement-type, .net-content {
    position: absolute;
    left: 54px;
    margin: 0;
    color: var(--ink);
    font-weight: 400;
    font-size: 15px;
  }
  .supplement-type { top: 22px; letter-spacing: 0.02em; }
  .net-content { top: 84px; }
  .supply {
    position: absolute;
    left: 400px;
    top: 30px;
    width: 160px;
    margin: 0;
    color: var(--ink);
    font-weight: 300;
    font-size: 23px;
    line-height: 32px;
    text-align: center;
  }
</style>
</head>
<body>
<div class="canvas">
  <section class="label">
    <div class="floral-decoration" role="img" aria-label="Faint teal chamomile flower illustration"></div>

    <div class="brand">
      <span class="brand-dot"></span>
      <span class="brand-name">Copperfield Vitals</span>
    </div>

    <h1 class="product-name">WILD<br>CHAMOMILE</h1>
    <p class="product-function">RELAXATION SUPPORT</p>

    <div class="rule r1"></div>
    <p class="description">Lorem ipsum dolor<br>Sit amet consectetur<br>Curabitur congue</p>

    <div class="rule r2"></div>
    <p class="benefit">IMPORVE SLEEPING PROCESS</p>

    <div class="rule r3"></div>
    <div class="facts-table">
      <div class="row-divider"></div>
      <div class="cell-divider"></div>
      <p class="supplement-type">DIETARY SUPPLEMENT</p>
      <p class="net-content">Net 1 fl oz/30ml e</p>
      <p class="supply">45 DAY<br>SUPPLY</p>
    </div>
    <div class="rule r4"></div>
  </section>
</div>
</body>
</html>
```